BRELDANO two folded A4 Product page design for exhibition

We are seeking a designer to create a visually captivating and informative two-folded A4 product page for Breldano Technologies. This page will be distributed at an exhibition to industry experts visiting our stand. Our aim is to showcase our technology-based solutions in the water industry, which is known for its traditional and regulated nature. The design should reflect solidity and professionalism while incorporating elements of our visual identity. We encourage you to draw inspiration from our website, www.breldano.lv, to gain a good understanding of Breldano's visual identity. Please refer to the attached demonstrator for relevant visuals and consider incorporating elements from our dashboard if it enhances the design and effectively conveys the message.

Design Requirements:

Size: Two-folded A4 format.
Visual Identity: Please refer to the website www.breldano.lv to familiarize yourself with our visual identity.
Industry Context: Keep in mind that the water industry is traditional, regulated, and somewhat old school.
Solid Appearance: Emphasize solidity and reliability in the design to instill confidence in our products.
Plain Style: Utilize a clean and straightforward design approach.
Layout: Create a well-structured layout where information is organized logically and intuitively.
Incorporate Visuals: Select appropriate visuals from the attached demonstrator and consider integrating relevant elements from our dashboard if it enhances the overall design and effectively communicates the message.

Deliverables:

Two-folded A4 product page design.
High-resolution digital files suitable for printing.

Timeline:
The design should be completed and ready for printing by Sunday evening.

Additional Notes:

Strive for a balanced combination of text and visuals to create an engaging and informative product page.
Incorporate Breldano's brand colors, fonts, and logo to maintain consistency with our visual identity.
The materials should exude a sense of solidity and professionalism to appeal to industry experts.

Target Market(s)

Water engineers

Industry/Entity Type

Water

Font styles to use
Sans Serif

Colors
0094D4
00A9DD
6FCCEA
C7EBF8
E9F6FB

Requirements
Must have
• Text and visual design incorporating product visuals

```html
<!DOCTYPE html>
<html lang="en">
<head>
<meta charset="utf-8">
<title>Breldano Technologies – Product Page</title>
<link rel="stylesheet" href="https://fonts.googleapis.com/css2?family=Arimo:wght@400;700&display=swap">
<style>
  :root {
    --royal: #1b3fe4;
    --sky-light: #4cc0ee;
    --pale: #c7ebf8;
    --ink: #1d1d1f;
    --white: #ffffff;
    --tick: #2aa84a;
  }
  * { box-sizing: border-box; margin: 0; padding: 0; }
  html, body { width: 1200px; height: 848px; overflow: hidden; background: var(--white); }
  body { font-family: "Arimo", Arial, sans-serif; color: var(--ink); }
  .page { position: relative; width: 1200px; height: 848px; overflow: hidden; }

  .hero-panel { position: absolute; left: 0; top: 0; width: 405px; height: 245px; }
  .hero-panel svg, .product-visual svg { display: block; }

  .block { position: absolute; }

  .heading {
    position: absolute; padding-left: 43px;
    color: var(--royal); font-weight: 400; font-size: 26px; line-height: 32.7px;
    white-space: nowrap;
  }
  .heading::before {
    content: ""; position: absolute; left: 1px; top: 10px;
    width: 13px; height: 13px; border-radius: 50%; background: var(--sky-light);
  }
  .heading.on-dark { color: var(--white); }
  .heading.on-dark::before { background: var(--pale); }

  .body-text { font-size: 12.9px; line-height: 17.25px; }
  .body-text p + p { margin-top: 17.25px; }

  .about-lead {
    position: absolute; color: var(--white); font-weight: 700;
    font-size: 16.4px; line-height: 23px;
  }

  .rule { position: absolute; width: 35px; height: 2px; background: var(--royal); }

  .case-title { color: var(--royal); font-weight: 700; font-size: 12.9px; line-height: 17.25px; }

  .checklist { position: absolute; list-style: none; }
  .checklist li {
    position: relative; padding-left: 25px;
    font-size: 14.3px; line-height: 18.6px; margin-bottom: 12.5px; white-space: nowrap;
  }
  .checklist li svg { position: absolute; left: 0; top: 2px; }

  .features p { font-size: 12.9px; line-height: 17.25px; }
  .features .key { color: var(--sky-light); font-weight: 700; }

  .product-visual { position: absolute; left: 405px; top: 675px; width: 405px; height: 173px; }
</style>
</head>
<body>
<div class="page">

  <div class="hero-panel" role="img" aria-label="Marbled blue water texture">
    <svg width="405" height="245" viewBox="0 0 405 245">
      <defs>
        <linearGradient id="marble" x1="0" y1="0" x2="1" y2="1">
          <stop offset="0" stop-color="#1d4fe6"/>
          <stop offset="0.45" stop-color="#1a3fe0"/>
          <stop offset="1" stop-color="#2b5cf0"/>
        </linearGradient>
      </defs>
      <polygon points="0,0 405,0 405,191 356,245 0,245" fill="url(#marble)"/>
    </svg>
  </div>

  <!-- Left column -->
  <h2 class="heading on-dark" style="left:49px; top:39px;">About Us</h2>
  <p class="about-lead" style="left:49px; top:79px; width:300px;">Breldano research and development is crafted by a team of leading scientists with extensive experience in water engineering, data science, information technology and business development.</p>

  <h2 class="heading" style="left:49px; top:274px;">What We Do</h2>
  <div class="block body-text" style="left:49px; top:313px; width:312px;">
    <p>We offer water utilities real-time control over drinking water quality, including automated monitoring, detection of contamination events, and cloud-based data analysis, providing proactive decision-making and reducing downtime and associated costs.</p>
  </div>

  <h2 class="heading" style="left:49px; top:423px;">Breldano Benefits</h2>
  <div class="block body-text" style="left:48px; top:462px; width:312px;">
    <p>Provides real-time data on minute-by-minute changes in water quality, allowing for continuous assessment of the impact of operational processes on water quality. This creates opportunities to improve the water quality management and audit monitoring programs.</p>
  </div>
  <div class="rule" style="left:49px; top:563px;"></div>
  <div class="block body-text" style="left:49px; top:577px; width:312px;">
    <p>Helps to facilitate proactive communication with drinking water consumers in cases of water quality deterioration, such as discolouration of water during firefighting events or repairment works of water distribution or treatment systems.</p>
  </div>
  <div class="rule" style="left:49px; top:675px;"></div>
  <div class="block body-text" style="left:49px; top:688px; width:312px;">
    <p>Regular measurements enable the planning of service works based on real-time water quality instead of relying on calendar-based maintenance plans.</p>
  </div>
  <div class="rule" style="left:49px; top:753px;"></div>
  <div class="block body-text" style="left:49px; top:769px; width:312px;">
    <p>Enables evaluation of the effectiveness of disinfection programs by assessing immediate changes in drinking water quality in real time.</p>
  </div>

  <!-- Middle column -->
  <h2 class="heading" style="left:437px; top:39px;">Use Cases of Breldano</h2>
  <div class="block body-text" style="left:437px; top:89px; width:345px;">
    <h3 class="case-title">Monitoring Drinking Water Quality:</h3>
    <p>The Breldano system provides real-time monitoring of water quality, enabling utilities to quickly detect any changes in water quality and take corrective action before they develop into larger problems.</p>
    <p>The fluctuations in water quality that occur throughout the day, week, and season create opportunities to optimise water treatment and distribution processes, from the water treatment to the end-user.</p>
  </div>
  <div class="rule" style="left:437px; top:275px;"></div>
  <div class="block body-text" style="left:437px; top:293px; width:345px;">
    <h3 class="case-title">Detection of Drinking Water Contamination:</h3>
    <p>The Breldano system is designed to detect contamination events in drinking water by monitoring five physicochemical water quality parameters, including turbidity, pH, conductivity, redox potential and temperature. Any changes detected by the system that indicate a potential contamination event can alert utilities to take quick action to protect public health.</p>
  </div>
  <div class="rule" style="left:437px; top:446px;"></div>
  <div class="block body-text" style="left:437px; top:464px; width:345px;">
    <h3 class="case-title">Management of Drinking Water Infrastructure:</h3>
    <p>The Breldano system can be used to monitor the performance of water treatment and distribution infrastructure, such as pumps, valves, pipelines, pumping stations, etc.</p>
    <p>By monitoring physicochemical parameters, the system can detect changes that may indicate a problem with an infrastructure, enabling utilities to quickly identify and address any issues to reduce downtime and associated costs to public health.</p>
  </div>

  <div class="product-visual" role="img" aria-label="Close-up of plastic water bottles with yellow caps">
    <svg width="405" height="173" viewBox="0 0 405 173">
      <defs>
        <radialGradient id="bottles" cx="0.55" cy="0.5" r="0.7">
          <stop offset="0" stop-color="#8a8a3a"/>
          <stop offset="0.5" stop-color="#3a3a30"/>
          <stop offset="1" stop-color="#1a1a18"/>
        </radialGradient>
      </defs>
      <polygon points="44,0 405,0 405,173 0,173 0,55" fill="url(#bottles)"/>
    </svg>
  </div>

  <!-- Right column -->
  <h2 class="heading" style="left:859px; top:39px;">Typical Problem<br>Situations to Use<br>Breldano</h2>
  <ul class="checklist" style="left:859px; top:149px;">
    <li><svg width="14" height="14" viewBox="0 0 15 15"><circle cx="7.5" cy="7.5" r="7.5" fill="var(--tick)"/><path d="M4 7.7l2.4 2.3L11 5.4" fill="none" stroke="#fff" stroke-width="2"/></svg>Repairs of water infrastructure</li>
    <li><svg width="14" height="14" viewBox="0 0 15 15"><circle cx="7.5" cy="7.5" r="7.5" fill="var(--tick)"/><path d="M4 7.7l2.4 2.3L11 5.4" fill="none" stroke="#fff" stroke-width="2"/></svg>Valve replacements</li>
    <li><svg width="14" height="14" viewBox="0 0 15 15"><circle cx="7.5" cy="7.5" r="7.5" fill="var(--tick)"/><path d="M4 7.7l2.4 2.3L11 5.4" fill="none" stroke="#fff" stroke-width="2"/></svg>Pipeline replacements</li>
    <li><svg width="14" height="14" viewBox="0 0 15 15"><circle cx="7.5" cy="7.5" r="7.5" fill="var(--tick)"/><path d="M4 7.7l2.4 2.3L11 5.4" fill="none" stroke="#fff" stroke-width="2"/></svg>Pump repairs</li>
    <li><svg width="14" height="14" viewBox="0 0 15 15"><circle cx="7.5" cy="7.5" r="7.5" fill="var(--tick)"/><path d="M4 7.7l2.4 2.3L11 5.4" fill="none" stroke="#fff" stroke-width="2"/></svg>Flushing of water distribution system</li>
    <li><svg width="14" height="14" viewBox="0 0 15 15"><circle cx="7.5" cy="7.5" r="7.5" fill="var(--tick)"/><path d="M4 7.7l2.4 2.3L11 5.4" fill="none" stroke="#fff" stroke-width="2"/></svg>Changes in operational mode</li>
    <li><svg width="14" height="14" viewBox="0 0 15 15"><circle cx="7.5" cy="7.5" r="7.5" fill="var(--tick)"/><path d="M4 7.7l2.4 2.3L11 5.4" fill="none" stroke="#fff" stroke-width="2"/></svg>Changes in chlorination process</li>
    <li><svg width="14" height="14" viewBox="0 0 15 15"><circle cx="7.5" cy="7.5" r="7.5" fill="var(--tick)"/><path d="M4 7.7l2.4 2.3L11 5.4" fill="none" stroke="#fff" stroke-width="2"/></svg>Non-typical changes in water<br>consumption patterns</li>
    <li><svg width="14" height="14" viewBox="0 0 15 15"><circle cx="7.5" cy="7.5" r="7.5" fill="var(--tick)"/><path d="M4 7.7l2.4 2.3L11 5.4" fill="none" stroke="#fff" stroke-width="2"/></svg>Flushing of filters</li>
    <li><svg width="14" height="14" viewBox="0 0 15 15"><circle cx="7.5" cy="7.5" r="7.5" fill="var(--tick)"/><path d="M4 7.7l2.4 2.3L11 5.4" fill="none" stroke="#fff" stroke-width="2"/></svg>Interruption of water flow</li>
    <li><svg width="14" height="14" viewBox="0 0 15 15"><circle cx="7.5" cy="7.5" r="7.5" fill="var(--tick)"/><path d="M4 7.7l2.4 2.3L11 5.4" fill="none" stroke="#fff" stroke-width="2"/></svg>Filter replacements</li>
    <li><svg width="14" height="14" viewBox="0 0 15 15"><circle cx="7.5" cy="7.5" r="7.5" fill="var(--tick)"/><path d="M4 7.7l2.4 2.3L11 5.4" fill="none" stroke="#fff" stroke-width="2"/></svg>Optimization of operational processes</li>
  </ul>

  <h2 class="heading" style="left:859px; top:545px;">Special Features</h2>
  <div class="block features" style="left:858px; top:592px; width:300px;">
    <p><span class="key">Portable design</span> enables easy installation and mobility.</p>
    <p><span class="key">Plug and play functionality</span> ensures simple and quick setup.</p>
    <p><span class="key">Real-time dashboard</span> provides easy monitoring of water quality parameters.</p>
    <p><span class="key">Cloud-based data analysis</span> offers comprehensive insights and trends.</p>
    <p><span class="key">Real-time alert system</span> immediately notifies of any anomalies or issues.</p>
    <p><span class="key">Integrate SCADA data</span> with water quality measurements.</p>
  </div>

</div>
</body>
</html>
```